Family Psychologist Needs a Sign Designed - Logo Supplied

I am looking for signage on the front window that is bright and catches people’s eyes as they drive past. Therefore, the writing can’t be too small that it is too hard to focus on and read from a moving car.

I want to maybe incorporate the floating spots somehow. I am also looking to hang a banner over the side of the front railing that lists what services are offered since the name doesn’t exactly cover it all . Services include: Psychology, Speech, OT. There is also an education component to the business where we do Study Skills Coaching to high school kids. I would like to see an option of this incorporated to but in a separate way so it isn’t associated with the “psychology” part of the business as this may deter people.

I also want to put a sign above the business in the overhead light thing (not sure what its called). Currently it is empty but the clinics next door have “chiropractor” and “medical centre” written in theirs so mine will have to be as equally simple but specific. Logo attached (EPS)

Ive also attached my logo and a few examples of where the signagewill go.

```html
<!DOCTYPE html>
<html lang="en">
<head>
<meta charset="utf-8">
<title>Learn Study Skills – Banner</title>
<link rel="stylesheet" href="https://fonts.googleapis.com/css2?family=Arimo:wght@700&display=swap">
<style>
  :root {
    --page-bg: #f2f2f0;
    --ink: #2b2a29;
    --halo: #ffffff;
    --lime: #d4de6a;
    --leaf: #9ccb6e;
    --green: #5cb37a;
    --teal: #4ca39a;
    --aqua: #55bccb;
    --sky: #96d3df;
  }
  html, body {
    margin: 0;
    padding: 0;
    width: 1200px;
    height: 517px;
    overflow: hidden;
    background: var(--page-bg);
  }
  .banner {
    position: absolute;
    left: 107px;
    top: 104px;
    width: 980px;
    height: 307px;
    overflow: hidden;
    background: linear-gradient(90deg,
      var(--lime) 0%,
      var(--leaf) 22%,
      var(--green) 36%,
      var(--teal) 46%,
      var(--aqua) 58%,
      var(--sky) 66%,
      var(--sky) 100%);
    box-shadow: 0 2px 6px rgba(0, 0, 0, 0.25);
  }
  .banner__emblem {
    position: absolute;
    left: 12px;
    top: 12px;
    width: 252px;
    height: 284px;
    border-radius: 48% 52% 30% 40% / 45% 50% 30% 40%;
    background: radial-gradient(circle at 45% 40%, rgba(120, 190, 140, 0.55), rgba(74, 159, 174, 0.55) 70%);
  }
  .banner__spots {
    position: absolute;
    left: 385px;
    top: 0;
    width: 380px;
    height: 307px;
    background: radial-gradient(ellipse at 60% 50%, rgba(255, 255, 255, 0.35), rgba(255, 255, 255, 0) 70%);
  }
  .banner__title {
    position: absolute;
    margin: 0;
    font-family: "Arimo", Arial, sans-serif;
    font-weight: 700;
    line-height: 1;
    color: var(--ink);
    white-space: nowrap;
    text-shadow: -3px 3px 0 var(--halo), -2px 2px 0 var(--halo), -1px 1px 0 var(--halo);
  }
  .banner__title--lead {
    left: 346px;
    top: 20px;
    font-size: 120px;
  }
  .banner__title--main {
    left: 64px;
    top: 146px;
    font-size: 125px;
  }
</style>
</head>
<body>
  <div class="banner">
    <div class="banner__emblem" role="img" aria-label="Outline of a head in profile with gears, the study skills emblem"></div>
    <div class="banner__spots" role="img" aria-label="Scattered floating spots in white and green"></div>
    <h1 class="banner__title banner__title--lead">Learn</h1>
    <p class="banner__title banner__title--main">STUDY SKILLS</p>
  </div>
</body>
</html>
```